Commercial Loan Originator Business Card (CHANGE COLORS SCHEME)

CHANGE COLOR SCHEME - SAME DESIGN

Name Miranda Lestock
Title Commercial Loan Originator
Office (800) 641-2905 x68
Direct (240) 731-2264
Email gardenpath4life@mailbox.example

Name Dale Fenwick
Office (800) 641-2905 x70
Direct (410) 392-6058
Email d.fenwickhomes@mailbox.example

Name Gerald Winslow
Office (800) 641-2905 x71
Direct (215) 946-3021
Email g.winslow63@mailbox.example

Name Joan Mallory
Office (800) 641-2905 x
Direct (202) 518-4467
Email jmallory74@mailbox.example

Name Norah Velasco
Office (800) 641-2905 x72
Direct (240) 867-1152
Email capitalhomelending@mailbox.example

```html
<!DOCTYPE html>
<html lang="en">
<head>
<meta charset="utf-8">
<title>Joan Mallory – Business Card</title>
<link href="https://fonts.googleapis.com/css2?family=Montserrat:wght@400;500;700;800&display=swap" rel="stylesheet">
<style>
  :root {
    --page-bg: #cfd9dd;
    --card-bg: #e6eef0;
    --card-edge: #f4f8f9;
    --ink: #16304a;
    --ink-soft: #2c4a5e;
    --accent: #2f7480;
    --portrait-top: #d6cfc4;
    --portrait-mid: #8a6a58;
    --portrait-low: #5a3b45;
  }
  * { box-sizing: border-box; margin: 0; padding: 0; }
  html, body {
    width: 1200px;
    height: 1047px;
    overflow: hidden;
    background: var(--page-bg);
    font-family: "Montserrat", Arial, sans-serif;
  }
  .business-card {
    position: absolute;
    left: 151px;
    top: 289px;
    width: 947px;
    height: 518px;
    background: var(--card-bg);
    border: 2px solid var(--card-edge);
    border-radius: 26px;
    overflow: hidden;
    box-shadow: 0 18px 40px rgba(22, 48, 74, 0.16);
  }
  .identity {
    position: absolute;
    left: 45px;
    top: 122px;
    width: 330px;
  }
  .name {
    font-weight: 800;
    font-size: 34px;
    letter-spacing: 0.3px;
    color: var(--ink);
    text-transform: uppercase;
    line-height: 1;
    white-space: nowrap;
  }
  .title {
    margin-top: 14px;
    font-weight: 500;
    font-size: 19px;
    color: var(--accent);
    white-space: nowrap;
  }
  .contacts {
    position: absolute;
    left: 45px;
    top: 286px;
    width: 335px;
    list-style: none;
  }
  .contact-item {
    display: flex;
    align-items: center;
    height: 37px;
    font-size: 18px;
    font-weight: 500;
    color: var(--ink-soft);
    white-space: nowrap;
  }
  .contact-icon {
    flex: none;
    width: 20px;
    height: 20px;
    margin-right: 10px;
    fill: var(--accent);
  }
  .portrait {
    position: absolute;
    left: 392px;
    top: 35px;
    width: 525px;
    height: 483px;
    background: linear-gradient(180deg, var(--portrait-top) 0%, var(--portrait-mid) 55%, var(--portrait-low) 100%);
  }
</style>
</head>
<body>
  <article class="business-card">
    <header class="identity">
      <h1 class="name">Joan Mallory</h1>
      <p class="title">Commercial Loan Originator</p>
    </header>

    <ul class="contacts">
      <li class="contact-item">
        <svg class="contact-icon" viewBox="0 0 24 24" aria-hidden="true">
          <path d="M3 9c0-2 4-4 9-4s9 2 9 4v2h-5V9.5c-1-.6-2.5-.9-4-.9s-3 .3-4 .9V11H3z"/>
          <path d="M6 12h12l2 7H4z"/>
        </svg>
        <span>(800) 641-2905 x</span>
      </li>
      <li class="contact-item">
        <svg class="contact-icon" viewBox="0 0 24 24" aria-hidden="true">
          <path d="M22 2 2 10l7 3 3 7zM9 13l9-8-6 10z" style="fill:none;stroke:var(--accent);stroke-width:2;stroke-linejoin:round"/>
        </svg>
        <span>(202) 518-4467</span>
      </li>
      <li class="contact-item">
        <svg class="contact-icon" viewBox="0 0 24 24" aria-hidden="true">
          <path d="M2 6h20v12H2z"/>
          <path d="M2 6l10 7 10-7" style="fill:none;stroke:var(--card-bg);stroke-width:1.6"/>
        </svg>
        <span>jmallory74@mailbox.example</span>
      </li>
    </ul>

    <div class="portrait" role="img" aria-label="Portrait photo of Joan Mallory, smiling, in a colourful patterned top"></div>
  </article>
</body>
</html>
```